Brivane - Business Cards for a new venture

create business card for a startup classified business dealing in construction materials, the cards need to have a professional look but modern, more serious than playful, one of the samples must include the official font (attached), please explore using the official colors in the company's logo

Target Market(s)

Energy sector

Contact Information for Business Card

Font styles to use
Other font styles liked:
• suissnord

Requirements
Must have
• corporate colors (in logo attached)
Nice to have
• Official font (in one of the samples) font is : suissnord
Should not have
• Cartoonish look

```html
<!DOCTYPE html>
<html lang="en">
<head>
<meta charset="utf-8">
<title>Brivane – Business Cards</title>
<link rel="stylesheet" href="https://fonts.googleapis.com/css2?family=Josefin+Sans:wght@400&family=Open+Sans:wght@400&display=swap">
<style>
  :root {
    --brand-blue: #0f4576;
    --navy-text: #1b3d6e;
    --mid-grey: #8e8e93;
    --text-grey: #5f5f63;
    --rule-lilac: #c9c6da;
    --card-white: #ffffff;
    --backdrop: #4b4b4d;
  }
  * { box-sizing: border-box; margin: 0; padding: 0; }
  html, body {
    width: 1200px; height: 1000px; overflow: hidden;
    background: var(--backdrop);
    font-family: "Open Sans", Arial, sans-serif;
  }
  .stage { position: relative; width: 1200px; height: 1000px; }
  .card {
    position: absolute; top: 170px; width: 398px; height: 665px;
    box-shadow: 0 4px 14px rgba(0,0,0,0.35);
  }
  .card--front { left: 172px; background: var(--brand-blue); }
  .card--back { left: 630px; background: var(--card-white); }

  .brand-name {
    position: absolute; left: 0; right: 0; text-align: center;
    font-family: "Open Sans", Arial, sans-serif; font-weight: 400;
    letter-spacing: 6px; text-transform: uppercase;
  }
  .card--front .brand-name { top: 355px; font-size: 40px; color: var(--card-white); }
  .card--back .brand-name { top: 165px; font-size: 38px; color: var(--brand-blue); }

  .details { position: absolute; left: 0; right: 0; top: 336px; text-align: center; }
  .person-name {
    font-family: "Josefin Sans", Arial, sans-serif; font-weight: 400;
    font-size: 23px; color: var(--navy-text); letter-spacing: 0.5px; line-height: 28px;
  }
  .person-role {
    font-family: "Josefin Sans", Arial, sans-serif;
    font-size: 17px; color: var(--text-grey); line-height: 22px; margin-top: 1px;
  }
  .rule { width: 46px; height: 1px; background: var(--rule-lilac); margin: 0 auto; }
  .rule--first { margin-top: 32px; }
  .phones { margin-top: 16px; }
  .phone-line {
    display: flex; justify-content: center; align-items: center; gap: 8px;
    font-size: 16px; color: var(--text-grey); line-height: 27px;
  }
  .phone-line svg { width: 14px; height: 14px; fill: var(--navy-text); }
  .rule--second { margin-top: 15px; }
  .email { margin-top: 15px; font-size: 16px; color: var(--text-grey); line-height: 24px; }
  .address { margin-top: 10px; font-size: 18px; color: var(--text-grey); line-height: 26px; letter-spacing: 0.4px; }
</style>
</head>
<body>
<main class="stage">
  <section class="card card--front" aria-label="Business card front">
    <div class="brand-name">Brivane</div>
  </section>

  <section class="card card--back" aria-label="Business card back">
    <div class="brand-name">Brivane</div>
    <div class="details">
      <h1 class="person-name">DANIEL ASHCROFT</h1>
      <p class="person-role">Managing Director</p>
      <div class="rule rule--first"></div>
      <div class="phones">
        <p class="phone-line">
          <svg viewBox="0 0 14 14" aria-hidden="true"><path d="M3.5 0h7a1 1 0 0 1 1 1v12a1 1 0 0 1-1 1h-7a1 1 0 0 1-1-1V1a1 1 0 0 1 1-1zm.6 1.6v9.6h5.8V1.6z"/></svg>
          <span>+999 99 999 9999</span>
        </p>
        <p class="phone-line">
          <svg viewBox="0 0 14 14" aria-hidden="true"><path d="M1 4.5C1 3 3.5 2 7 2s6 1 6 2.5v1h-3V4.2H4v1.3H1zM3 6.5h8l1.5 5.5h-11zM7 7.6a1.7 1.7 0 1 0 0 3.4 1.7 1.7 0 0 0 0-3.4z"/></svg>
          <span>+999 99 999 9999</span>
        </p>
      </div>
      <div class="rule rule--second"></div>
      <p class="email">info@brivane.com</p>
      <p class="address">2275 Harbor Mill Road<br>Dayton, Ohio 45402</p>
    </div>
  </section>
</main>
</body>
</html>
```